Website Design for Pearlvista.TV

The Pearlvista website will provide users with current Chinese news, entertainment, and information. The site will have both textual and video content similar to vqz.com, jxw.com and other popular news sites.

The site will have similar content to chi

```html
<!DOCTYPE html>
<html lang="en">
<head>
<meta charset="utf-8">
<title>Pearlvista.TV</title>
<link rel="stylesheet" href="https://fonts.googleapis.com/css2?family=Arimo:wght@400;700&family=PT+Serif:wght@400;700&display=swap">
<style>
:root{
  --blue:#1f3f94; --blue-dark:#14307a; --page:#e4e4e4; --ink:#222; --muted:#666;
  --red:#c4161c; --link:#2b4a8a; --dark:#2a2a2a; --darker:#1f1f1f; --line:#d6d6d6;
  --white:#fff; --panel:#f7f7f7;
}
*{box-sizing:border-box;margin:0;padding:0}
html,body{width:1200px;height:2555px;overflow:hidden}
body{background:var(--page);font-family:"Arimo",Arial,sans-serif;color:var(--ink);position:relative}
.site{position:absolute;left:65px;top:0;width:1075px;height:2555px;background:var(--white)}
.serif{font-family:"PT Serif",Georgia,serif}
/* header */
.masthead{height:87px;background:linear-gradient(#2648a6,var(--blue-dark));position:relative}
.logo{position:absolute;left:20px;top:20px;color:var(--white);font-size:36px;letter-spacing:-.5px}
.clock{position:absolute;left:262px;top:18px;background:var(--red);color:#fff;font-size:12px;padding:2px 4px}
.datebar{position:absolute;right:20px;top:14px;font-size:13px;font-weight:700;color:#fff}
.datebar span{color:#9fc0ff}
.nav{height:36px;background:#1c1c1c;display:flex;padding-left:20px;align-items:flex-end}
.nav a{color:#eee;font-size:15px;padding:0 18px;height:36px;line-height:36px;border-right:1px solid #3a3a3a;text-decoration:none}
.nav a.on{background:#f2f2f2;color:var(--blue);height:30px;line-height:30px}
.search{margin-left:auto;margin-right:20px;align-self:center;width:220px;height:22px;background:#fff;border:1px solid #999;font-size:12px;color:#999;padding:3px 6px;position:relative}
.search svg{position:absolute;right:4px;top:3px}
.subnav{height:37px;display:flex;align-items:center;justify-content:space-between;padding:0 22px;border-bottom:1px solid var(--line);font-size:11px}
.subnav span{color:#333}
.subnav i{color:#999;font-style:normal}
/* placeholders */
.ph{position:relative;overflow:hidden}
.cap{position:absolute;left:0;right:0;bottom:0;background:rgba(0,0,0,.72);color:#fff;font-size:14px;line-height:17px;padding:5px 10px}
.tag{position:absolute;right:0;top:0;color:#fff;font-size:12px;padding:3px 9px}
/* spotlight */
.spotlight{height:400px;background:var(--dark);position:relative}
.spot-grid{position:absolute;left:20px;top:20px;width:1032px;height:320px;display:grid;grid-template-columns:267px 297px 271px 183px;grid-template-rows:160px 156px;gap:4px}
.spot-grid .big{grid-row:span 2}
.spot-title{position:absolute;left:20px;top:342px;font-size:30px;color:#fff;font-weight:700}
.spot-title span{color:#aaa}
.dots{position:absolute;left:530px;top:367px;display:flex;gap:5px}
.dots b{width:6px;height:6px;border-radius:50%;background:#888}.dots b:first-child{background:#fff}
.arrow{position:absolute;top:333px;width:34px;height:34px;border-radius:50%;background:#fff;border:1px solid #ccc;display:flex;align-items:center;justify-content:center}
/* top stories */
.top{height:367px;position:relative;border-bottom:1px solid var(--line)}
.top-list{position:absolute;left:20px;top:30px;width:222px}
.sec-h{font-size:24px;font-weight:700;text-align:right;border-bottom:1px solid var(--line);padding-bottom:8px;margin-bottom:14px}
.sec-h span{color:#999}
.story h3{font-family:"PT Serif",Georgia,serif;font-weight:400;color:var(--red);font-size:15px;line-height:19px;margin-bottom:10px}
.story p{font-size:12px;line-height:16px;margin-bottom:14px}
.video{position:absolute;left:292px;top:43px;width:392px;height:293px;background:linear-gradient(160deg,#8a8a84,#3e3d3a 60%,#6b6a66)}
.play{position:absolute;left:163px;top:110px;width:70px;height:70px;border-radius:50%;background:rgba(255,255,255,.35);display:flex;align-items:center;justify-content:center}
.thumbs{position:absolute;left:0;right:0;bottom:0;height:48px;background:#111;display:flex;gap:10px;padding:9px 8px}
.thumbs i{flex:1;background:linear-gradient(#7a6a55,#3a3530)}
.ad-label{position:absolute;left:704px;top:22px;font-size:12px;color:#777}
.ad{position:absolute;left:704px;top:43px;width:348px;height:293px;background:#e6e6e6;padding:10px}
.ad-in{background:#fff;height:100%;position:relative}
.phone{position:absolute;left:30px;top:25px;width:108px;height:220px;border-radius:14px;background:#111}
.screen{position:absolute;left:8px;top:22px;right:8px;bottom:30px;background:linear-gradient(#c03a2b,#6d8a3f 50%,#3c5b8a)}
.ad-brand{position:absolute;left:178px;top:42px;font-size:18px;color:var(--blue)}
.ad-brand b{display:inline-block;width:12px;height:12px;background:var(--blue);margin-right:6px}
.ad-copy{position:absolute;left:163px;top:98px;width:170px;text-align:center;font-size:21px;line-height:27px;color:#333}
.badge{position:absolute;left:190px;top:165px;width:118px;height:46px;border:1px solid #bbb;border-radius:4px;background:#f4f4f4}
.ad-dl{position:absolute;left:163px;top:225px;width:170px;text-align:center;font-size:13px}
/* section bars */
.bar{height:52px;background:linear-gradient(#353535,#222);display:flex;align-items:center;padding:0 20px;color:#fff}
.bar h2{font-family:"PT Serif",Georgia,serif;font-size:21px;font-weight:700}
.bar h2 span{color:#aaa}
.bar nav{margin-left:auto;display:flex;gap:24px;font-size:11px}
.block{height:495px;position:relative;border-bottom:1px solid var(--line)}
.lead{position:absolute;left:20px;top:26px;width:350px}
.lead .frame{background:#fff;box-shadow:0 0 4px rgba(0,0,0,.3);padding:10px;height:260px}
.lead .frame .ph{height:240px}
.lead h3{font-family:"PT Serif",Georgia,serif;color:var(--link);font-size:16px;line-height:19px;margin:20px 10px 14px}
.lead p{font-size:12px;line-height:16px;margin:0 14px 0 10px}
.tiles{position:absolute;left:408px;top:26px;width:276px;display:flex;flex-direction:column;gap:5px}
.tiles .ph{height:106px}
.tiles .cap{font-size:12px;padding:4px 8px}
.side{position:absolute;left:736px;top:20px;width:303px}
.thumbgrid{display:grid;grid-template-columns:1fr 1fr;gap:6px 35px;padding:0 2px 10px;border-bottom:1px solid var(--line)}
.th .ph{height:100px;border:1px solid #ccc}
.th p{font-size:10px;font-style:italic;color:var(--link);text-align:center;line-height:13px;margin-top:2px}
.links li{list-style:none;border-bottom:1px solid var(--line);font-size:15px;line-height:19px;padding:10px 32px 10px 0;position:relative}
.links li:after{content:"›";position:absolute;right:0;top:12px;width:16px;height:16px;border-radius:50%;background:#eee;color:#777;font-size:12px;line-height:15px;text-align:center}
/* picks */
.picks{height:213px;background:#ececec;position:relative;padding:14px 22px}
.picks h4{font-size:10px;color:#555;font-weight:400;margin-bottom:6px}
.pick-row{display:flex;gap:9px}
.pick{width:163px}
.pick .ph{height:114px;border:3px solid #fff;box-shadow:0 0 2px rgba(0,0,0,.3)}
.pick .cap{font-size:12px;padding:3px 8px}
.pick p{color:var(--link);font-size:14px;line-height:18px;margin:8px 4px 0}
.copyband{height:58px;background:linear-gradient(#4a4a4a,#3a3a3a);color:#fff;padding:14px 20px;font-size:21px}
.copyband span{color:#aaa}
.foot{height:197px;background:var(--dark);position:relative;color:#888;font-size:10px;line-height:13px}
.foot h5{font-family:"PT Serif",Georgia,serif;font-size:18px;color:#bbb;font-weight:700;margin-bottom:14px}
.fcol{position:absolute;top:38px}
.fcol a{color:#ddd}
.fcol li{list-style:none;color:#ddd;line-height:18px}
.links-foot{height:60px;background:var(--darker);color:#bbb;font-size:10px;line-height:13px;text-align:center;padding:10px 40px;border-top:1px solid #444}
</style>
</head>
<body>
<div class="arrow" style="left:16px"><svg width="12" height="12" viewBox="0 0 12 12"><path d="M8 1 3 6l5 5" fill="none" stroke="#333" stroke-width="2"/></svg></div>
<div class="arrow" style="left:1152px"><svg width="12" height="12" viewBox="0 0 12 12"><path d="M4 1l5 5-5 5" fill="none" stroke="#333" stroke-width="2"/></svg></div>

<div class="site">
  <header class="masthead">
    <div class="logo">Pearlvista.TV</div>
    <div class="clock">13:40</div>
    <div class="datebar">112.1.15 Pearlvista | <span>Weather&gt;&gt; Harbin -10 C ~ -19</span></div>
  </header>
  <nav class="nav">
    <a class="on">Home</a><a>News</a><a>Sports</a><a>Entertainment</a><a>Guests</a><a>Pearlvista</a><a>Weather</a><a>Selected</a>
    <div class="search">Search...<svg width="14" height="14" viewBox="0 0 14 14"><circle cx="6" cy="6" r="4.5" fill="none" stroke="#333" stroke-width="1.6"/><path d="M9.5 9.5 13 13" stroke="#333" stroke-width="1.8"/></svg></div>
  </nav>
  <div class="subnav">
    <span>REGIONAL</span><i>|</i><span>CUSTOMS</span><i>|</i><span>CHINESE BUSINESSMEN</span><i>|</i><span>BRAND CHINA</span><i>|</i><span>CUISINE</span><i>|</i><span>ARCHAEOLOGICAL DISCOVERIES</span><i>|</i><span>ACROSS CHINA</span><i>|</i><span>CHINESE CULTURE</span>
  </div>

  <section class="spotlight">
    <div class="spot-grid">
      <div class="ph big" role="img" aria-label="Street scene with old buildings and a car" style="background:linear-gradient(#c9a25a,#6d5a3c 45%,#4b6f8c 75%,#333)"><span class="tag" style="background:#e3c21a;color:#111">News</span><div class="cap">UK economy creates 130,000 jobs in the car industry.</div></div>
      <div class="ph" role="img" aria-label="Guitarist performing on stage" style="background:linear-gradient(135deg,#5a1020,#b3306b 50%,#2a0a12)"><span class="tag" style="background:var(--red)">Entertainment</span><div class="cap">A new sensation in music today:<br>Crazy Kline</div></div>
      <div class="ph" role="img" aria-label="Young athlete sitting" style="background:linear-gradient(135deg,#b79a50,#8a6c3a 50%,#d7b870)"><span class="tag" style="background:#3a8a2a">Sport</span><div class="cap">How do young people see the future of sports in our country?</div></div>
      <div class="ph big" role="img" aria-label="Satellite dish against the sky" style="background:linear-gradient(#6f93b8,#c6d3df 50%,#55606a)"><span class="tag" style="background:#6a1a8a">Local</span><div class="cap">Protester blocked off Planetarium gates</div></div>
      <div class="ph" role="img" aria-label="Newspaper page about investing" style="background:linear-gradient(#dcdcdc,#9a9a9a)"><span class="tag" style="background:#2a3a9a">Business</span><div class="cap">Best stock to invest in this year.<br>Tips from the top investment firms.</div></div>
      <div class="ph" role="img" aria-label="Pile of medicine capsules" style="background:linear-gradient(135deg,#e4dcb0,#9f9868 60%,#605a3a)"><span class="tag" style="background:#a0135a">Health</span><div class="cap">What is going to happen with the farmaceutical industry?</div></div>
    </div>
    <div class="spot-title serif"><span>In The</span> Spotlight</div>
    <div class="dots"><b></b><b></b><b></b><b></b></div>
  </section>

  <section class="top">
    <div class="top-list">
      <div class="sec-h serif"><span>Top</span> Stories</div>
      <div class="story"><h3>China's first large-scale reintroduction of pandas</h3><p>The country's first large-scale reintroduction panda on January 11 about the official launch, through the layers selected, the Chengdu Giant...</p></div>
      <div class="story"><h3>Giant dragon Dragon Dance Chinese New Year record</h3><p>Yesterday, a baby from the 200,000 photos makes up three-storey giant dragon, brought to life "take off" in the Yongding Gate Square, breaking...</p></div>
    </div>
    <div class="video ph" role="img" aria-label="Video still of a temple gate with stone lion">
      <div class="play"><svg width="26" height="30" viewBox="0 0 26 30"><path d="M2 2l22 13L2 28z" fill="rgba(255,255,255,.7)"/></svg></div>
      <div class="thumbs"><i></i><i></i><i></i><i></i><i></i><i></i></div>
    </div>
    <div class="ad-label">Advertisement</div>
    <div class="ad"><div class="ad-in">
      <div class="phone"><div class="screen" role="img" aria-label="App screen with travel photos"></div></div>
      <div class="ad-brand"><b></b>Pearlvista</div>
      <div class="ad-copy">The ultimate<br>travel companion</div>
      <div class="badge"></div>
      <div class="ad-dl">Download now</div>
    </div></div>
  </section>

  <div class="bar"><h2><span>Today,</span> Regional</h2><nav><span>TODAY, REGIONAL</span><span>ACROSS CHINA</span><span>CHINESE CULTURE</span></nav></div>
  <section class="block">
    <div class="lead">
      <div class="frame"><div class="ph" role="img" aria-label="Sunset over a river plain" style="background:linear-gradient(#f04a1a,#f7a020 45%,#c8250e 60%,#6a0e05)"></div></div>
      <h3>Fertile land of magnificent beauty of the Central Plains</h3>
      <p>The set to the Great Wall and the Yellow River in the Central Plains as the center, the lens that once swept through the Chinese ancient civilization gave birth to...</p>
    </div>
    <div class="tiles">
      <div class="ph" role="img" aria-label="Monks at a memorial hall opening" style="background:linear-gradient(#a9c4de,#c87a3a 55%,#7a2a1a)"><div class="cap">Guang Shan Buddha Memorial Hall Opening</div></div>
      <div class="ph" role="img" aria-label="Village gate among trees" style="background:linear-gradient(#b9d6ef,#5f8f3a 60%,#3a5a22)"><div class="cap">Beijing beautiful country - Volume village...</div></div>
      <div class="ph" role="img" aria-label="Aerial view of a coastal city" style="background:linear-gradient(#7e97ad,#4d6a85 60%,#324a5e)"><div class="cap">"Coastal Line": the son of the Yellow River</div></div>
      <div class="ph" role="img" aria-label="Oranges on a tree" style="background:linear-gradient(#4e6a2a,#d9a12a 60%,#7a5a1a)"><div class="cap">Chinese state banquet Fu Orange</div></div>
    </div>
    <div class="side">
      <div class="thumbgrid">
        <div class="th"><div class="ph" role="img" aria-label="Tibetan temple under blue sky" style="background:linear-gradient(#2a6ad0,#8ab4e8 55%,#8a4a1a)"></div><p>The mystery of snow<br>in Tibet</p></div>
        <div class="th"><div class="ph" role="img" aria-label="Mountain with pink blossoms" style="background:linear-gradient(#dfe8f2,#7f8a7a 50%,#d04a6a)"></div><p>Tao Holy Mountain<br>Lushan and Humanities</p></div>
        <div class="th"><div class="ph" role="img" aria-label="Tibetan temple under blue sky" style="background:linear-gradient(#2a6ad0,#8ab4e8 55%,#8a4a1a)"></div><p>The mystery of snow<br>in Tibet</p></div>
        <div class="th"><div class="ph" role="img" aria-label="Ancient mural painting" style="background:linear-gradient(135deg,#b58a4a,#6a4a2a 60%,#a03a2a)"></div><p>"The sky in Tibet":<br>the memory of ancestors</p></div>
      </div>
      <ul class="links"><li>Casual city wear - China ningjing</li><li>Winter snow line: record of liquefuied natural gas</li><li>"Geography China" Urban Shadow</li></ul>
    </div>
  </section>

  <div class="bar"><h2><span>Today,</span> Chinese Businessmen</h2><nav><span>CHINESE BUSINESSMEN</span><span>SPOTLIGHT</span><span>FAMOUS STYLE</span></nav></div>
  <section class="block">
    <div class="lead">
      <div class="frame"><div class="ph" role="img" aria-label="Portrait of a reporter in a blue jacket before a red door" style="background:linear-gradient(90deg,#8a1a14,#5a2a1a 50%,#6a7a4a)"></div></div>
      <h3>Lin Haoshen - Images recorded with China</h3>
      <p>He is a reporter with a camera to write the history of the Soviet Union; he is a journalist, more than a dozen countries in the Allied Wire Service bureau; but he said dismissively: I just raised the camera spectator, to the real history...</p>
    </div>
    <div class="tiles">
      <div class="ph" role="img" aria-label="Monks at a memorial hall opening" style="background:linear-gradient(#a9c4de,#c87a3a 55%,#7a2a1a)"><div class="cap">Guang Shan Buddha Memorial Hall Opening</div></div>
      <div class="ph" role="img" aria-label="Village gate among trees" style="background:linear-gradient(#b9d6ef,#5f8f3a 60%,#3a5a22)"><div class="cap">Beijing beautiful country - Volume village...</div></div>
      <div class="ph" role="img" aria-label="Aerial view of a coastal city" style="background:linear-gradient(#7e97ad,#4d6a85 60%,#324a5e)"><div class="cap">"Coastal Line": the son of the Yellow River</div></div>
      <div class="ph" role="img" aria-label="Oranges on a tree" style="background:linear-gradient(#4e6a2a,#d9a12a 60%,#7a5a1a)"><div class="cap">Chinese state banquet Fu Orange</div></div>
    </div>
    <div class="side">
      <div class="thumbgrid">
        <div class="th"><div class="ph" role="img" aria-label="Tibetan temple under blue sky" style="background:linear-gradient(#2a6ad0,#8ab4e8 55%,#8a4a1a)"></div><p>The mystery of snow<br>in Tibet</p></div>
        <div class="th"><div class="ph" role="img" aria-label="Mountain with pink blossoms" style="background:linear-gradient(#dfe8f2,#7f8a7a 50%,#d04a6a)"></div><p>Tao Holy Mountain<br>Lushan and Humanities</p></div>
        <div class="th"><div class="ph" role="img" aria-label="Tibetan temple under blue sky" style="background:linear-gradient(#2a6ad0,#8ab4e8 55%,#8a4a1a)"></div><p>The mystery of snow<br>in Tibet</p></div>
        <div class="th"><div class="ph" role="img" aria-label="Ancient mural painting" style="background:linear-gradient(135deg,#b58a4a,#6a4a2a 60%,#a03a2a)"></div><p>"The sky in Tibet":<br>the memory of ancestors</p></div>
      </div>
      <ul class="links"><li>Casual city wear - China ningjing</li><li>Winter snow line: record of liquefuied natural gas</li><li>"Geography China" Urban Shadow</li></ul>
    </div>
  </section>

  <section class="picks">
    <h4>EDITOR'S PICKS</h4>
    <div class="pick-row">
      <div class="pick"><div class="ph" role="img" aria-label="Newspaper page about investing" style="background:linear-gradient(#e2e2e2,#9a9a9a)"></div><p>Top stock to invest in this year</p></div>
      <div class="pick"><div class="ph" role="img" aria-label="Airliner landing over a runway" style="background:linear-gradient(#c8d2dc,#9aa4ae 70%,#5a6a4a)"></div><p>Airlines of choice for most in the UK</p></div>
      <div class="pick"><div class="ph" role="img" aria-label="Guitarist performing on stage" style="background:linear-gradient(135deg,#5a1020,#b3306b 50%,#2a0a12)"><div class="cap">▶ Play video</div></div><p>Latest sensation in music: Crazy Kline</p></div>
      <div class="pick"><div class="ph" role="img" aria-label="Ancient arch ruins" style="background:linear-gradient(#8fb4d8,#a8a088 60%,#6a6454)"><div class="cap">▣ View slideshow</div></div><p>Prehystoric artifacts discovered in Rome</p></div>
      <div class="pick"><div class="ph" role="img" aria-label="Black and white sculpture" style="background:linear-gradient(135deg,#bbb,#555 60%,#999)"><div class="cap">▣ View slideshow</div></div><p>Art Mama</p></div>
      <div class="pick"><div class="ph" role="img" aria-label="Young athlete sitting" style="background:linear-gradient(135deg,#b79a50,#8a6c3a 50%,#d7b870)"></div><p>How young people see the future</p></div>
    </div>
  </section>

  <div class="copyband serif"><span>Copyright © 2012</span> Pearlvista</div>
  <footer class="foot">
    <div class="fcol" style="left:20px"><h5>Contact</h5>E-mail: desk@pearlvista.tv<br>Tel: 00-10-00000000<br>ICP No. 00000000<br>Video Distribution License No.: 0,000,000</div>
    <div class="fcol" style="left:387px"><h5>Content</h5><ul><li>» News</li><li>» Entertainment</li><li>» Sports</li><li>» Guests</li><li>» Pearlvista</li></ul></div>
    <div class="fcol" style="left:737px"><h5>Copyright</h5>2012 Copyright © Pearlvista Media Group<br>All Rights Reserved.<br><a>Home | About | Work | Services | Blog</a><br><a>Contact | Sitemap | Terms &amp; Privacy</a></div>
  </footer>
  <div class="links-foot">Larkfield Broadband | Northwind Video | Lantern Live | Orchid Broadband | Riverline | Kestrel Broadband | Jadeport Finance | Cobalt Sports | Tidewater Net | rule of law, the Chinese media | Meadow Net<br>safety net interest Brightpath Network | Amberlight News | Inkstone Gallery | Harbor Entertainment | Tileway | Skyward first sports | Willowgate Heritage | Reedbank Audio<br>Primrose Video | Frostline Video | Crimson Academy | Arena Clips | Open Wave Radio | Chinese medicine | Bellreed Music | Lantern video</div>
</div>
</body>
</html>
```